new business card design - modern, professional, bold, B2B focus - with QR code pls

we are looking for a modern looking, colorful, business card design. some highlights:
- put space for QR code please. probably on the back but I'm open.
- biz card to be orientated VERTICAL not the traditional horizontal.
- do NOT use our full name on the card (ie: Allied Furnace Servicing Inc). Use only AFS Inc or AFS.
- use black and orange with some white. ideally black card with orange and white for the letters/logo etc. gray ok too - for outlines etc.
- we work in HEAVY industrial, so the cards should lend itself to this. our website is alfurnace.example, so you can see what we do.
- do NOT put in little smoke stack pictures / silouettes etc.
- think MODERN and INDUSTRIAL, with a techy focus.

Industry/Entity Type

heavy industrial - all of them. we perform maintenance and inspection services at heavy industrial and commercial businesses. so B2B

Contact Information for Business Card

name, title, phone numbers (cell + hardline), website, email address. of course our logo too - either on front or front and back.

Font styles to use
Other font styles liked:
• montserrat

Colors
F0912C
F2A743
F7CA91
FBE8D2
FDF5EE

Requirements
Must have
• see description
Nice to have
• see description
Should not have
• see description

```html
<!DOCTYPE html>
<html lang="en">
<head>
<meta charset="utf-8">
<title>AFS Inc – Business Card</title>
<link href="https://fonts.googleapis.com/css2?family=Montserrat:wght@300;400;600;900&display=swap" rel="stylesheet">
<style>
  :root {
    --page-bg: #ffffff;
    --card-bg: #3a3a3c;
    --orange: #f7991f;
    --white: #ffffff;
    --stone: #c8c1b8;
  }
  * { margin: 0; padding: 0; box-sizing: border-box; }
  html, body {
    width: 1200px;
    height: 1200px;
    overflow: hidden;
    background: var(--page-bg);
    font-family: "Montserrat", sans-serif;
  }
  .canvas {
    position: relative;
    width: 1200px;
    height: 1200px;
  }
  .card {
    position: absolute;
    top: 185px;
    width: 498px;
    height: 830px;
    background: var(--card-bg);
    overflow: hidden;
  }
  .card--front { left: 69px; }
  .card--back { left: 633px; }

  .brand-name {
    position: absolute;
    font-family: "Montserrat", sans-serif;
    font-weight: 900;
    color: var(--orange);
    line-height: 1;
    letter-spacing: -3px;
    white-space: nowrap;
  }
  .card--front .brand-name {
    left: 88px;
    top: 254px;
    font-size: 155px;
  }
  .card--back .brand-name {
    left: 113px;
    top: 434px;
    font-size: 148px;
  }

  .holder-name {
    position: absolute;
    right: 64px;
    top: 560px;
    font-size: 32px;
    font-weight: 600;
    line-height: 1.2;
    color: var(--orange);
    white-space: nowrap;
  }

  .contact-list {
    position: absolute;
    right: 64px;
    top: 637px;
    list-style: none;
  }
  .contact-item {
    display: flex;
    align-items: center;
    justify-content: flex-end;
    gap: 22px;
    height: 34px;
    font-size: 19px;
    font-weight: 400;
    color: var(--white);
    white-space: nowrap;
  }
  .contact-icon {
    width: 22px;
    height: 22px;
    flex: none;
  }

  .site-vertical {
    position: absolute;
    left: 78px;
    top: 267px;
    height: 296px;
    writing-mode: vertical-rl;
    transform: rotate(180deg);
    font-size: 27px;
    font-weight: 300;
    line-height: 1.2;
    color: var(--white);
    letter-spacing: 0.5px;
    text-align: left;
    white-space: nowrap;
  }

  .qr-space {
    position: absolute;
    right: 67px;
    bottom: 68px;
    width: 110px;
    height: 110px;
    border: 2px solid var(--stone);
  }
</style>
</head>
<body>
<main class="canvas">

  <section class="card card--front" aria-label="Business card front">
    <div class="brand-name">AFS</div>

    <p class="holder-name">Marlowe Keegan</p>

    <ul class="contact-list">
      <li class="contact-item">
        <span class="contact-text">905-555-0142</span>
        <svg class="contact-icon" viewBox="0 0 24 24" aria-hidden="true">
          <circle cx="12" cy="12" r="12" fill="var(--orange)"/>
          <path d="M8.6 6.5l1.6 2.4-1 1.2c.7 1.5 1.8 2.6 3.3 3.3l1.2-1 2.4 1.6-.6 1.7c-4.2-.3-7.5-3.6-7.8-7.8z" fill="var(--white)"/>
        </svg>
      </li>
      <li class="contact-item">
        <span class="contact-text">P: 877-555-0199</span>
        <svg class="contact-icon" viewBox="0 0 24 24" aria-hidden="true">
          <circle cx="12" cy="12" r="12" fill="var(--orange)"/>
          <path d="M8.6 6.5l1.6 2.4-1 1.2c.7 1.5 1.8 2.6 3.3 3.3l1.2-1 2.4 1.6-.6 1.7c-4.2-.3-7.5-3.6-7.8-7.8z" fill="var(--white)"/>
        </svg>
      </li>
      <li class="contact-item">
        <span class="contact-text">www.alfurnace.example</span>
        <svg class="contact-icon" viewBox="0 0 24 24" aria-hidden="true">
          <circle cx="12" cy="12" r="12" fill="var(--orange)"/>
          <circle cx="12" cy="12" r="5.5" fill="none" stroke="var(--white)" stroke-width="1.4"/>
          <ellipse cx="12" cy="12" rx="2.3" ry="5.5" fill="none" stroke="var(--white)" stroke-width="1.2"/>
          <line x1="6.5" y1="12" x2="17.5" y2="12" stroke="var(--white)" stroke-width="1.2"/>
        </svg>
      </li>
      <li class="contact-item">
        <span class="contact-text">afsinc@alfurnace.example</span>
        <svg class="contact-icon" viewBox="0 0 24 24" aria-hidden="true">
          <circle cx="12" cy="12" r="12" fill="var(--orange)"/>
          <rect x="6.5" y="8" width="11" height="8" rx="1" fill="var(--white)"/>
          <path d="M6.8 8.4L12 12.4l5.2-4" fill="none" stroke="var(--orange)" stroke-width="1.1"/>
        </svg>
      </li>
    </ul>
  </section>

  <section class="card card--back" aria-label="Business card back">
    <p class="site-vertical">alfurnace.example</p>
    <div class="brand-name">AFS</div>
    <div class="qr-space" role="img" aria-label="Space reserved for QR code"></div>
  </section>

</main>
</body>
</html>
```